Vitamin B12 Liquid Drops Label

hi, i need a label designed for my vitamin b12 drops that i am going to be selling on bazaroo. the label needs to quickly capture the attention of a buyer as he or she is scrolling through the thumbnail search results on bazaroo.example my brand is called zulpa. i already have an example brand logo i will be using, however, i need help designing the rest of the label. attached are some examples of labels i like for other supplements.some of these examples are pink. i do not want pink. please go for a blue/green color scheme. THE DESIGN MUST BE BOLD

Target Market(s)

adults ages 30 - 64

Font styles to use
Sans Serif

Colors
0455a3
cedeed
3176b5
85acd3
cfdeed
9bcb3b
abd037
cadf82
00a990

Requirements
Must have
• - bold design
• - somewhat gender-neutral color scheme because this will be used equally by men and women
• - B12 MUST be very prominent and visible on the label
Should not have
• - it should not be "crunchy" looking

```html
<!DOCTYPE html>
<html lang="en">
<head>
<meta charset="utf-8">
<title>Zulpa Vitamin B12 Drops – Packaging</title>
<link rel="stylesheet" href="https://fonts.googleapis.com/css2?family=Open+Sans:wght@700;800&display=swap">
<style>
  :root {
    --backdrop: #e6e8ea;
    --carton-green: #9bcb3b;
    --carton-blue: #3176b5;
    --carton-blue-deep: #0455a3;
    --label-green: #abd037;
    --label-blue: #0455a3;
    --pale-green: #cadf82;
  }
  * { margin: 0; padding: 0; box-sizing: border-box; }
  html, body {
    width: 1200px;
    height: 800px;
    overflow: hidden;
    background: var(--backdrop);
    font-family: "Open Sans", Arial, sans-serif;
  }
  .packaging {
    position: relative;
    width: 1200px;
    height: 800px;
  }
  .carton-front {
    position: absolute;
    left: 250px;
    top: 70px;
    width: 320px;
    height: 660px;
  }
  .bottle-label {
    position: absolute;
    left: 640px;
    top: 190px;
    width: 330px;
    height: 412px;
  }
  .brand-name { font-weight: 800; letter-spacing: 1px; }
  .product-name { font-weight: 800; }
  .ingredient { font-weight: 700; letter-spacing: 4px; }
</style>
</head>
<body>
<main class="packaging">

  <svg class="carton-front" viewBox="0 0 320 660" aria-label="Carton front panel">
    <rect class="carton-base" width="320" height="660" fill="var(--carton-green)"/>
    <rect class="carton-top-band" width="320" height="40" fill="var(--carton-blue)"/>
    <polygon class="carton-lower-chevron" points="0,476 118,441 320,560 320,658 0,499" fill="var(--carton-blue-deep)"/>
    <polygon class="carton-title-band" points="0,363 320,231 320,345 0,477" fill="var(--carton-blue)"/>
    <text class="brand-name" x="160" y="262" transform="rotate(-22 160 240)"
          text-anchor="middle" font-size="70" fill="var(--carton-blue-deep)">ZULPA</text>
    <text class="product-name" x="160" y="374" transform="rotate(-22 160 356)"
          text-anchor="middle" font-size="46" fill="var(--pale-green)">VITAMIN B12</text>
  </svg>

  <svg class="bottle-label" viewBox="0 0 330 412" aria-label="Dropper bottle label">
    <rect class="label-base" width="330" height="412" fill="var(--label-blue)"/>
    <polygon class="label-green-field" points="0,0 330,0 240,220 0,220" fill="var(--label-green)"/>
    <text class="product-name" x="12" y="209" font-size="31" fill="var(--label-blue)">VITAMIN B12</text>
    <text class="ingredient" x="14" y="244" font-size="12" fill="var(--pale-green)">METHYLCOBAMALIN</text>
    <text class="brand-name" x="312" y="370" text-anchor="end" font-size="32" fill="var(--label-green)">ZULPA</text>
  </svg>

</main>
</body>
</html>
```